We sell companies excess stock for them

We need a business card for a company based in New Zealand called 'StockHarbor'.

Check out our website to get an idea www.stockharbor.example

We help other businesses to;
- Sell Excess Stock
- Manage Product Returns
- Sell Company Assets

Our logo is attached for your reference
The font used is 'RifficFree-Bold'

Target Market(s)

Businesses

Industry/Entity Type

Business

Contact Information for Business Card

Name: Mark Pellow
Phone: 027 846 2093
email: markpellow@stockharbor.example
website: www.stockharbor.example

Font styles to use
Other font styles liked:
• Unsure

Colors
9bcb3b

Requirements
Must have
• coming soon
Nice to have
• coming soon
Should not have
• coming soon

```html
<!DOCTYPE html>
<html lang="en">
<head>
<meta charset="utf-8">
<title>StockHarbor Business Card</title>
<link rel="stylesheet" href="https://fonts.googleapis.com/css2?family=Open+Sans:wght@400;600;700;800&display=swap">
<style>
  :root {
    --page-bg: #e9eaec;
    --card-bg: #ffffff;
    --brand-green: #7cb32b;
    --brand-green-light: #9bcb3b;
    --ink-dark: #2f2f2f;
    --ink-body: #4a4a4a;
    --art-warm: #f2b066;
  }
  * { margin: 0; padding: 0; box-sizing: border-box; }
  html, body {
    width: 1200px; height: 970px; overflow: hidden;
    background: var(--page-bg);
    font-family: "Open Sans", Arial, sans-serif;
  }
  .business-card {
    position: absolute; left: 60px; top: 185px;
    width: 1080px; height: 600px;
    background: var(--card-bg);
    overflow: hidden;
    box-shadow: 0 6px 24px rgba(0,0,0,0.12);
  }
  .green-panel {
    position: absolute; right: 0; top: 0;
    width: 265px; height: 100%;
    background: var(--brand-green);
  }
  .mascot-art {
    position: absolute; left: 610px; top: 8px;
    width: 450px; height: 584px;
    background: linear-gradient(160deg, rgba(155,203,59,0.55) 0%, rgba(242,176,102,0.75) 50%, rgba(124,179,43,0.9) 100%);
    border-radius: 24px;
  }
  .brand-name {
    position: absolute; left: 60px; top: 84px;
    font-size: 62px; font-weight: 800; letter-spacing: -1.5px;
    color: var(--ink-dark); line-height: 1;
  }
  .contact-block { position: absolute; left: 74px; top: 232px; width: 520px; color: var(--ink-body); }
  .person-name {
    font-size: 30px; font-weight: 600; color: var(--brand-green);
    letter-spacing: 0.5px; line-height: 1.15;
  }
  .person-role { font-size: 23px; line-height: 1.3; }
  .address { margin-top: 22px; font-size: 23px; line-height: 1.4; }
  .contact-list { list-style: none; margin-top: 18px; font-size: 22px; line-height: 1.45; }
  .contact-list li { display: flex; align-items: center; gap: 12px; white-space: nowrap; }
  .contact-list svg { width: 22px; height: 22px; fill: var(--brand-green); flex: none; }
</style>
</head>
<body>
  <main class="business-card">
    <div class="green-panel"></div>
    <div class="mascot-art" role="img" aria-label="Cartoon delivery mascot in a green cap and overalls giving a thumbs up while carrying an orange parcel"></div>

    <div class="brand-name">StockHarbor</div>

    <section class="contact-block">
      <div class="person-name">MARK PELLOW</div>
      <div class="person-role">Managing Director</div>
      <div class="address">Harbour Lane, Riverton,<br>Northland, 0471</div>
      <ul class="contact-list">
        <li>
          <svg viewBox="0 0 24 24" aria-hidden="true"><path d="M3 8c0-2 4-4 9-4s9 2 9 4v2h-5V8H8v2H3zM6 11h12l2 9H4z"/></svg>
          027 846 2093
        </li>
        <li>
          <svg viewBox="0 0 24 24" aria-hidden="true"><path d="M7 3h10v5H7zM4 9h16v8h-3v4H7v-4H4zm5 6v4h6v-4z"/></svg>
          + 000 000 0000
        </li>
        <li>
          <svg viewBox="0 0 24 24" aria-hidden="true"><path d="M3 6h18v12H3zm2 2v.4l7 5 7-5V8z"/></svg>
          markpellow@stockharbor.example
        </li>
        <li>
          <svg viewBox="0 0 24 24" aria-hidden="true"><circle cx="12" cy="12" r="9"/><path d="M3 12h18M12 3c3 3 3 15 0 18M12 3c-3 3-3 15 0 18" stroke="#fff" stroke-width="1.4" fill="none"/></svg>
          www.stockharbor.example
        </li>
      </ul>
    </section>
  </main>
</body>
</html>
```